Disability and mental health support work company requires business card

Specialising
Wrenfield Disability is a new QCAP service aimed toward QCAP participants with a history of criminal justice, psychosocial/mental health, intellectual, and cognitive disabilities.

Our focus
Focusing on providing core QCAP supports for community participation, daily activities and supported independent living.

Authentic
Likeminded people wanting to make a difference in participant's lives.

Our aim to provide holistic and empowering supports targeted towards creating independence and guidance for all participants and families.
Over 35 years of experience working with people that have psychosocial, intellectual, and cognitive disabilities.

Industry/Entity Type

disability and mental health

Contact Information for Business Card

logo - business name

Colors
0054AA
0677BA
7BADD7
CADEEF
E8F1F8
FFF300
FFF600
FEFA6F
FFFEC7
FFFEE8

Requirements
Must have
• want double sided business cards(wont let me change it)
Should not have
• any disability related pictures

```html
<!DOCTYPE html>
<html lang="en">
<head>
<meta charset="UTF-8">
<title>Wrenfield Disability – Business Card</title>
<link href="https://fonts.googleapis.com/css2?family=Montserrat:wght@400;600;700&display=swap" rel="stylesheet">
<style>
  :root {
    --navy: #1e3a5c;
    --navy-deep: #182f4b;
    --gold: #f2b62a;
    --gold-soft: #e8c46c;
    --white: #ffffff;
    --page: #f3f3f3;
  }
  * { box-sizing: border-box; margin: 0; padding: 0; }
  html, body {
    width: 800px;
    height: 1200px;
    overflow: hidden;
    background: var(--page);
    font-family: "Montserrat", Arial, sans-serif;
  }
  .sheet {
    width: 800px;
    height: 1200px;
    display: flex;
    flex-direction: column;
    align-items: center;
    justify-content: center;
    gap: 60px;
  }
  .card {
    position: relative;
    width: 700px;
    height: 390px;
    overflow: hidden;
    box-shadow: 0 6px 18px rgba(0,0,0,0.12);
  }
  .card-art {
    position: absolute;
    inset: 0;
  }
  .brand-name {
    position: absolute;
    width: 240px;
    text-align: center;
    color: var(--gold-soft);
    font-weight: 600;
    font-size: 24px;
    letter-spacing: 2px;
    line-height: 1.3;
    text-transform: uppercase;
  }
  .card-front .brand-name { left: 80px; top: 164px; }
  .card-back .brand-name { left: 190px; top: 159px; }

  .person {
    position: absolute;
    left: 375px;
    top: 64px;
  }
  .person-name {
    color: var(--white);
    font-weight: 700;
    font-size: 30px;
    letter-spacing: 0.5px;
    text-transform: uppercase;
  }
  .person-title {
    color: var(--gold);
    font-weight: 400;
    font-size: 19px;
    margin-top: 4px;
  }
  .contact-list {
    position: absolute;
    left: 375px;
    top: 178px;
    list-style: none;
    color: var(--white);
    font-size: 17px;
    font-weight: 400;
  }
  .contact-item {
    display: flex;
    align-items: flex-start;
    gap: 14px;
    margin-bottom: 20px;
    line-height: 1.4;
  }
  .contact-icon {
    width: 14px;
    height: 14px;
    margin-top: 4px;
    flex: none;
  }
</style>
</head>
<body>
<main class="sheet">

  <section class="card card-front" aria-label="Card front">
    <svg class="card-art" viewBox="0 0 700 390" aria-hidden="true">
      <rect width="700" height="390" fill="var(--navy)"/>
      <path d="M0 0 H255 C310 120 300 270 200 390 H0 Z" fill="var(--gold)"/>
      <circle cx="200" cy="200" r="128" fill="var(--navy-deep)"/>
      <circle cx="200" cy="200" r="118" fill="var(--navy)" stroke="#3a5778" stroke-width="2"/>
    </svg>
    <div class="brand-name">Wrenfield<br>Disability</div>

    <div class="person">
      <h1 class="person-name">Marcus Hale</h1>
      <p class="person-title">Title</p>
    </div>

    <ul class="contact-list">
      <li class="contact-item">
        <svg class="contact-icon" viewBox="0 0 24 24" aria-hidden="true"><path fill="var(--gold)" d="M6.6 10.8a15.1 15.1 0 0 0 6.6 6.6l2.2-2.2c.3-.3.7-.4 1-.2 1.1.4 2.3.6 3.6.6.6 0 1 .4 1 1V20c0 .6-.4 1-1 1A17 17 0 0 1 3 4c0-.6.4-1 1-1h3.5c.6 0 1 .4 1 1 0 1.3.2 2.5.6 3.6.1.3 0 .7-.2 1z"/></svg>
        <span>+000-1234-5678</span>
      </li>
      <li class="contact-item">
        <svg class="contact-icon" viewBox="0 0 24 24" aria-hidden="true"><path fill="var(--gold)" d="M2 5h20v14H2z"/><path d="M2 5l10 8 10-8" fill="none" stroke="var(--navy)" stroke-width="2"/></svg>
        <span>youremail@email.com</span>
      </li>
      <li class="contact-item">
        <svg class="contact-icon" viewBox="0 0 24 24" aria-hidden="true"><path fill="var(--gold)" d="M12 2a7 7 0 0 0-7 7c0 5 7 13 7 13s7-8 7-13a7 7 0 0 0-7-7zm0 9.5A2.5 2.5 0 1 1 12 6.5a2.5 2.5 0 0 1 0 5z"/></svg>
        <span>123 Main Street<br>11th Floor, Some City</span>
      </li>
    </ul>
  </section>

  <section class="card card-back" aria-label="Card back">
    <svg class="card-art" viewBox="0 0 700 390" aria-hidden="true">
      <rect width="700" height="390" fill="var(--navy)"/>
      <path d="M700 0 H440 C390 120 395 270 500 390 H700 Z" fill="var(--gold)"/>
      <circle cx="310" cy="195" r="128" fill="var(--navy-deep)"/>
      <circle cx="310" cy="195" r="118" fill="var(--navy)" stroke="#3a5778" stroke-width="2"/>
    </svg>
    <div class="brand-name">Wrenfield<br>Disability</div>
  </section>

</main>
</body>
</html>
```